Commercial printing and sign company printed advertisement.

We're wanting a new look for our printed advertisements. We've been in business for 40 years and have been pushing hard the last couple of years to grow our business. Our target market is changing and our client base is changing. I am looking for advertisement that appeals to larger companies. However, we are not stuffy people so I would like the ads to convey our professionalism but also stand out with color and have a fun side. I'm currently needing advertisements for a printed magazine, printed newspaper, web ads and a table top at a local restaurant. We have our traditional four color logo (swoosh) as well as a simpler single color option. I am attaching various ads we have done previously so you can see what we have. It is important for these ads to convey the different things we do - as we do alot!

```html
<!DOCTYPE html>
<html lang="en">
<head>
<meta charset="utf-8">
<title>Brightline Printing – Printing &amp; Sign Company</title>
<link href="https://fonts.googleapis.com/css2?family=Oswald:wght@400;500;700&family=Kaushan+Script&display=swap" rel="stylesheet">
<style>
  :root{
    --page-bg:#d6d6d8;
    --white:#ffffff;
    --blue:#20479b;
    --red:#cf1f2e;
    --ink:#1d1d1f;
    --panel:#e6f4fc;
    --check:#a6c23a;
    --yellow-band:#f2c417;
    --orange-a:#ee7423;
    --orange-b:#f5ab24;
    --pill-a:#3d8fd6;
    --pill-b:#0b5cad;
    --badge-purple:#7b4fb0;
    --badge-blue:#3a62b8;
    --badge-teal:#3bb0a6;
    --badge-yellow:#f3cf3a;
    --badge-pink:#e55aa0;
  }
  *{margin:0;padding:0;box-sizing:border-box}
  html,body{width:1200px;height:1117px;overflow:hidden;background:var(--page-bg)}
  .ad{position:absolute;left:193px;top:86px;width:814px;height:945px;background:var(--white);overflow:hidden;font-family:"Oswald",sans-serif}
  .ad-background{position:absolute;left:0;top:0;width:814px;height:945px}
  .headline{position:absolute;left:66px;font-weight:700;line-height:1;white-space:nowrap;letter-spacing:-0.5px}
  .headline--top{top:246px;font-size:85px;color:var(--blue)}
  .headline--bottom{top:332px;font-size:82px;color:var(--red)}
  .slogan-pill{position:absolute;left:68px;top:432px;width:464px;height:45px;border-radius:23px;
    background:linear-gradient(90deg,var(--pill-a),var(--pill-b));color:var(--white);
    font-weight:700;font-size:29px;line-height:45px;text-align:center;letter-spacing:-0.3px}
  .brand-name{position:absolute;left:580px;top:255px;width:217px;text-align:center;color:var(--red);
    font-weight:700;font-size:36px;line-height:1.05}
  .brand-name .brand-mark{display:block;width:26px;height:26px;margin:0 auto 12px;background:var(--red)}
  .service-list{position:absolute;left:85px;top:515px;width:490px;list-style:none;
    display:grid;grid-template-columns:185px 1fr;row-gap:7px}
  .service-list li{display:flex;align-items:center;height:40px;font-size:30px;font-weight:400;color:var(--ink);white-space:nowrap;letter-spacing:-0.3px}
  .service-list svg{width:17px;height:17px;margin-right:13px;flex:none}
  .anniversary-badge{position:absolute;left:552px;top:472px;width:214px;height:172px;border-radius:50%;
    background:radial-gradient(circle at 65% 50%,var(--badge-yellow) 0%,var(--badge-pink) 35%,var(--badge-blue) 70%,var(--badge-teal) 100%);
    opacity:.55}
  .tagline{position:absolute;left:0;top:785px;width:814px;text-align:center;color:var(--white);
    font-family:"Kaushan Script",cursive;font-size:50px;line-height:1.2;text-shadow:1px 2px 2px rgba(120,60,0,.45)}
  .contact-line{position:absolute;left:0;top:866px;width:814px;display:flex;justify-content:center;align-items:center;
    gap:6px;color:var(--white);font-size:22px;font-weight:400;white-space:nowrap;letter-spacing:-0.3px}
  .contact-line svg{width:16px;height:16px;flex:none}
</style>
</head>
<body>
<main class="ad">
  <svg class="ad-background" viewBox="0 0 1348 1565" preserveAspectRatio="none">
    <defs>
      <linearGradient id="photoTones" x1="0" y1="0" x2="1" y2="0.3">
        <stop offset="0" stop-color="#f4f0ea"/>
        <stop offset="0.3" stop-color="#e9d9b8"/>
        <stop offset="0.45" stop-color="#e7a83c"/>
        <stop offset="0.62" stop-color="#8f8e98"/>
        <stop offset="0.85" stop-color="#c9c7cf"/>
        <stop offset="1" stop-color="#e3e2e6"/>
      </linearGradient>
      <linearGradient id="greenBand" x1="0" y1="0" x2="1" y2="0">
        <stop offset="0" stop-color="#b1c030"/>
        <stop offset="0.3" stop-color="#e2e6a0"/>
        <stop offset="0.5" stop-color="#b5c332"/>
        <stop offset="1" stop-color="#9fbf2e"/>
      </linearGradient>
      <linearGradient id="orangeField" x1="0" y1="0" x2="1" y2="0.4">
        <stop offset="0" stop-color="#ee7423"/>
        <stop offset="1" stop-color="#f5ab24"/>
      </linearGradient>
      <linearGradient id="swatchTones" x1="0" y1="0" x2="1" y2="1">
        <stop offset="0" stop-color="#3dbf8a"/>
        <stop offset="0.25" stop-color="#f2d22c"/>
        <stop offset="0.5" stop-color="#e9423f"/>
        <stop offset="0.75" stop-color="#c13a9c"/>
        <stop offset="1" stop-color="#4a46b8"/>
      </linearGradient>
    </defs>
    <g role="img" aria-label="Photo of a print technician loading vinyl rolls beside a wide-format printer">
      <path d="M0 0H1348V85C1100 230 700 330 400 330C250 330 100 300 0 275Z" fill="url(#photoTones)"/>
    </g>
    <path class="band-green" d="M0 275C100 300 250 330 400 330C700 330 1100 230 1348 85V115C1100 265 700 372 400 380C250 382 100 360 0 335Z" fill="url(#greenBand)"/>
    <path class="band-yellow" d="M820 342C1050 300 1250 200 1348 122V170C1200 255 1000 325 820 342Z" fill="var(--yellow-band)"/>
    <path class="orange-field" d="M0 1092Q60 1060 140 1050H1348V1565H0Z" fill="url(#orangeField)"/>
    <rect class="services-panel" x="85" y="825" width="952" height="435" rx="30" fill="var(--panel)"/>
    <circle class="badge-backdrop" cx="1112" cy="908" r="258" fill="var(--white)"/>
    <g role="img" aria-label="Photo of a fanned-out colour swatch guide">
      <path d="M1348 1002C1250 1040 1150 1130 1115 1220C1108 1262 1150 1286 1230 1288L1348 1290Z" fill="url(#swatchTones)"/>
    </g>
  </svg>

  <h1>
    <span class="headline headline--top">A PRINTING &amp;</span>
    <span class="headline headline--bottom">SIGN COMPANY</span>
  </h1>

  <div class="brand-name"><span class="brand-mark"></span>BRIGHTLINE<br>PRINTING</div>

  <p class="slogan-pill">ONE STOP, ONE SHOP, DOING IT ALL!</p>

  <ul class="service-list">
    <li><svg viewBox="0 0 20 20"><circle cx="10" cy="10" r="10" fill="var(--check)"/><path d="M5.5 10.2l3 3 6-6" fill="none" stroke="#fff" stroke-width="2.4" stroke-linecap="round" stroke-linejoin="round"/></svg>SIGNS</li>
    <li><svg viewBox="0 0 20 20"><circle cx="10" cy="10" r="10" fill="var(--check)"/><path d="M5.5 10.2l3 3 6-6" fill="none" stroke="#fff" stroke-width="2.4" stroke-linecap="round" stroke-linejoin="round"/></svg>SCREEN PRINTING</li>
    <li><svg viewBox="0 0 20 20"><circle cx="10" cy="10" r="10" fill="var(--check)"/><path d="M5.5 10.2l3 3 6-6" fill="none" stroke="#fff" stroke-width="2.4" stroke-linecap="round" stroke-linejoin="round"/></svg>BANNERS</li>
    <li><svg viewBox="0 0 20 20"><circle cx="10" cy="10" r="10" fill="var(--check)"/><path d="M5.5 10.2l3 3 6-6" fill="none" stroke="#fff" stroke-width="2.4" stroke-linecap="round" stroke-linejoin="round"/></svg>EMBROIDERY</li>
    <li><svg viewBox="0 0 20 20"><circle cx="10" cy="10" r="10" fill="var(--check)"/><path d="M5.5 10.2l3 3 6-6" fill="none" stroke="#fff" stroke-width="2.4" stroke-linecap="round" stroke-linejoin="round"/></svg>POSTER</li>
    <li><svg viewBox="0 0 20 20"><circle cx="10" cy="10" r="10" fill="var(--check)"/><path d="M5.5 10.2l3 3 6-6" fill="none" stroke="#fff" stroke-width="2.4" stroke-linecap="round" stroke-linejoin="round"/></svg>PROMO ITEMS</li>
    <li><svg viewBox="0 0 20 20"><circle cx="10" cy="10" r="10" fill="var(--check)"/><path d="M5.5 10.2l3 3 6-6" fill="none" stroke="#fff" stroke-width="2.4" stroke-linecap="round" stroke-linejoin="round"/></svg>DECALS</li>
    <li><svg viewBox="0 0 20 20"><circle cx="10" cy="10" r="10" fill="var(--check)"/><path d="M5.5 10.2l3 3 6-6" fill="none" stroke="#fff" stroke-width="2.4" stroke-linecap="round" stroke-linejoin="round"/></svg>PRINTING</li>
    <li><svg viewBox="0 0 20 20"><circle cx="10" cy="10" r="10" fill="var(--check)"/><path d="M5.5 10.2l3 3 6-6" fill="none" stroke="#fff" stroke-width="2.4" stroke-linecap="round" stroke-linejoin="round"/></svg>BLUE PRINTS</li>
    <li><svg viewBox="0 0 20 20"><circle cx="10" cy="10" r="10" fill="var(--check)"/><path d="M5.5 10.2l3 3 6-6" fill="none" stroke="#fff" stroke-width="2.4" stroke-linecap="round" stroke-linejoin="round"/></svg>DESIGN &amp; SO MUCH MORE!</li>
  </ul>

  <div class="anniversary-badge" role="img" aria-label="Anniversary badge celebrating 40 years in business, 1985 to 2025"></div>

  <p class="tagline">A team Your Can Trust Since 1985</p>

  <p class="contact-line">
    <svg viewBox="0 0 16 16"><path d="M8 1a5 5 0 0 0-5 5c0 3.8 5 9 5 9s5-5.2 5-9a5 5 0 0 0-5-5zm0 7a2 2 0 1 1 0-4 2 2 0 0 1 0 4z" fill="#fff"/></svg>
    <span>2450 Maple Avenue | Cedar Falls, MO |</span>
    <svg viewBox="0 0 16 16"><circle cx="8" cy="8" r="7" fill="#fff"/><g fill="none" stroke="var(--orange-a)" stroke-width="1"><ellipse cx="8" cy="8" rx="3" ry="6"/><line x1="2" y1="8" x2="14" y2="8"/><line x1="3" y1="5" x2="13" y2="5"/><line x1="3" y1="11" x2="13" y2="11"/></g></svg>
    <span>www.brightlineprinting.com |</span>
    <svg viewBox="0 0 16 16"><circle cx="8" cy="8" r="8" fill="#fff"/><path d="M5.2 4.2l1.4-.4 1 2.2-.9.7a5 5 0 0 0 2.6 2.6l.7-.9 2.2 1-.4 1.4c-3.6.3-6.9-3-6.6-6.6z" fill="var(--orange-a)"/></svg>
    <span>555-014-2290</span>
  </p>
</main>
</body>
</html>
```